Business Card Design Project

We need a business card for our IT services provider business. We provide services to small and medium business, and would like something that reflects the color scheme / branding on our recently updated website - www.tallobrix.com.au

The card type we have chosen is a matte laminated double sided configuration at 86mm x 54mm on 350 GSM cardboard.
Updates

Target Market(s)

Small and Medium Business owners

Industry/Entity Type

Business

Requirements
Must have
• *Details on all cards*

Company Name: Tallobrix Pty Ltd
ABN: 52 683 914 207
Address: 47-49 Pembury Street, Ashcombe Vale, Victoria 3172
Phone: 1300 GRAB UP
Fax: 03 9417 6258
Website: www.tallobrix.com.au
Logo/Handprint Icon

*Person Specific*

```html
<!DOCTYPE html>
<html lang="en">
<head>
<meta charset="utf-8">
<title>Tallobrix Business Card</title>
<link rel="stylesheet" href="https://fonts.googleapis.com/css2?family=Arimo:wght@400;700&display=swap">
<style>
  :root {
    --page-bg-light: #e9e9e9;
    --page-bg-dark: #b9b9b9;
    --card-blue-light: #1f6bad;
    --card-blue: #17558f;
    --card-blue-dark: #0f3f6e;
    --emblem-blue: #0e3b66;
    --text-white: #ffffff;
    --text-soft: #e6eef7;
  }
  * { box-sizing: border-box; margin: 0; padding: 0; }
  html, body {
    width: 1200px;
    height: 900px;
    overflow: hidden;
  }
  body {
    background: radial-gradient(ellipse at 50% 45%, var(--page-bg-light) 0%, var(--page-bg-dark) 100%);
    font-family: "Arimo", Arial, sans-serif;
    display: flex;
    flex-direction: column;
    align-items: center;
    justify-content: center;
    gap: 56px;
  }
  .card {
    position: relative;
    width: 560px;
    height: 352px;
    background: radial-gradient(ellipse at 50% 40%, var(--card-blue-light) 0%, var(--card-blue) 55%, var(--card-blue-dark) 100%);
    color: var(--text-white);
    box-shadow: 0 10px 26px rgba(0, 0, 0, 0.28);
    overflow: hidden;
  }

  /* Front face */
  .card-front .brand {
    position: absolute;
    top: 132px;
    left: 0;
    right: 0;
    display: flex;
    align-items: center;
    justify-content: center;
    gap: 12px;
  }
  .brand-mark {
    width: 14px;
    height: 14px;
    background: var(--text-white);
  }
  .brand-name {
    font-size: 38px;
    font-weight: 400;
    letter-spacing: 2px;
    color: var(--text-white);
  }
  .card-front .website {
    position: absolute;
    top: 250px;
    left: 0;
    right: 0;
    text-align: center;
    font-size: 14px;
    letter-spacing: 0.5px;
    color: var(--text-soft);
  }

  /* Back face */
  .card-back .emblem-area {
    position: absolute;
    left: 56px;
    top: 70px;
    width: 150px;
    height: 190px;
    border-radius: 50%;
    background: radial-gradient(ellipse at center, rgba(14, 59, 102, 0.55) 0%, rgba(14, 59, 102, 0) 70%);
  }
  .card-back .person {
    position: absolute;
    left: 78px;
    top: 196px;
  }
  .person-name {
    font-size: 23px;
    font-weight: 400;
    margin-bottom: 6px;
  }
  .person-detail {
    font-size: 14px;
    line-height: 1.35;
    color: var(--text-soft);
  }
  .card-back .company {
    position: absolute;
    right: 34px;
    top: 52px;
    text-align: right;
    font-size: 13px;
    line-height: 1.5;
    color: var(--text-soft);
  }
</style>
</head>
<body>

  <section class="card card-front" aria-label="Card front">
    <div class="brand">
      <span class="brand-mark"></span>
      <span class="brand-name">Tallobrix</span>
    </div>
    <p class="website">www.tallobrix.com.au</p>
  </section>

  <section class="card card-back" aria-label="Card back">
    <div class="emblem-area" role="img" aria-label="Faint brand emblem decoration"></div>
    <div class="person">
      <p class="person-name">John Doe</p>
      <p class="person-detail">555 555 555</p>
      <p class="person-detail">name@surname.com</p>
    </div>
    <address class="company" style="font-style: normal;">
      <p>Tallobrix Pty Ltd</p>
      <p>ABN: 52 683 914 207</p>
      <p>47-49 Pembury Street,</p>
      <p>Ashcombe Vale, Victoria 3172</p>
      <p>Phone: 1300 GRAB UP</p>
      <p>Fax: 03 9417 6258</p>
    </address>
  </section>

</body>
</html>
```